CREATE A KILLER WEBSITE DESIGN

We are a firearms training company that trains CIVILIANS (no police or military pictures - thank you!) to defend themselves and are looking for a killer design that's clean, easy to navigate and modern! We want the newest trends applied to this sight like a scrollable site so you can scroll down and see all the features. We are okay with tweaking the HTML but need the artistic design to look good. I'll provide a link to our current site along with a sight we really like so you can get an idea!

I'm supplying a PowerPoint Design we are going with from another designer so you can match the style to the new site.

PAGES: (Please use information from our current site. We like the information but just want a more polished look similar to the NWDLA site below but in our colors.)
Home - Long Form Scrolling Site. Top fold will be a video with a play button.
Falcon Institute - Seven Level Training Program Info Page That Will Contain A Video.
Contact Us - This will be a page that DOES NOT CONTAIN AN EMAIL ADDRESS. Just a contact us form
Meet The Trainer: Morgan Pellbrook

Our site:
https://www.brisklanewardens.biz

Sights We Like:
https://www.nwdefenseleague.example.com
https://quorvel.example.com
https://brantforgeworks.example.com
https://www.pelnrigear.example.com

Target Market(s)

Men and women ages 21 to 100 years old

Industry/Entity Type

Self Defense

Number of Pages Required

5+ page

Font styles to use
Sans Serif

Colors
f26267

Requirements
Must have
• Clean and engaging. Use of colors that match our logo.
Should not have
• Poor design quality

```html
<!DOCTYPE html>
<html lang="en">
<head>
<meta charset="utf-8">
<title>Brisklane Wardens — Firearms Training for Civilians</title>
<link rel="stylesheet" href="https://fonts.googleapis.com/css2?family=Rajdhani:wght@600;700&family=Open+Sans:ital,wght@0,400;0,600;0,700;1,400&display=swap">
<style>
:root{
  --red:#e3262d;
  --ink:#111113;
  --dark:#1a1a1c;
  --mid:#2a2a2d;
  --grey:#8c8c90;
  --light:#f4f4f4;
  --line:#e2e2e2;
  --white:#ffffff;
  --head:'Rajdhani', sans-serif;
  --body:'Open Sans', sans-serif;
}
*{box-sizing:border-box;margin:0;padding:0}
html,body{width:1200px;height:2684px;overflow:hidden}
body{font-family:var(--body);color:#333;background:var(--white);font-size:13px}
.page{position:relative;width:1200px;height:2684px}

/* top bar */
.topbar{position:absolute;top:0;left:0;right:0;height:50px;display:flex;align-items:center;padding:0 60px;z-index:5;background:rgba(10,10,12,.85)}
.brand{display:flex;align-items:center;gap:8px;color:var(--white);font-family:var(--head);font-weight:700;font-size:17px;letter-spacing:1px;text-transform:uppercase}
.brand .dot{width:18px;height:18px;border-radius:50%;background:var(--red)}
.contact-mini{display:flex;gap:18px;margin-left:60px;color:#cfcfcf;font-size:10px}
.contact-mini span{display:flex;align-items:center;gap:5px}
.nav{display:flex;gap:26px;margin-left:60px;font-size:11px;color:var(--white)}
.search{margin-left:auto;width:120px;height:24px;background:#2b2b2e;border-radius:2px;color:#888;font-size:10px;display:flex;align-items:center;padding:0 8px}
.btn{display:inline-block;font-family:var(--body);font-weight:700;font-size:10px;letter-spacing:.5px;text-transform:uppercase;padding:9px 16px;border-radius:2px}
.btn-red{background:var(--red);color:var(--white)}
.btn-white{background:var(--white);color:var(--red)}
.topbar .btn{margin-left:14px;padding:7px 14px}

/* hero */
.hero{position:absolute;top:0;left:0;width:1200px;height:440px;background:radial-gradient(ellipse at 70% 40%,#3a3a3e 0%,#18181a 55%,#0c0c0d 100%)}
.hero-visual{position:absolute;left:560px;top:90px;width:520px;height:300px;border-radius:6px;background:linear-gradient(135deg,#4a4a4f,#222225 70%)}
.play{position:absolute;width:40px;height:40px;border-radius:50%;background:var(--white);display:flex;align-items:center;justify-content:center}
.hero .play{left:820px;top:250px}
.hero h1{position:absolute;left:120px;top:130px;font-family:var(--head);font-weight:700;font-size:66px;line-height:60px;color:var(--white)}
.hero h1 em{font-style:normal;color:var(--red)}
.hero .actions{position:absolute;left:120px;top:340px;display:flex;gap:14px}

/* about */
.about{position:absolute;top:440px;left:0;width:1200px;height:460px;background:var(--white)}
.portrait{position:absolute;left:150px;top:40px;width:200px;height:230px;background:linear-gradient(180deg,#c9c9c9,#7d7d7d)}
.about-text{position:absolute;left:410px;top:44px;width:620px}
.eyebrow{font-family:var(--head);font-weight:600;font-size:17px;color:var(--red)}
.about-text h2{font-family:var(--head);font-weight:700;font-size:30px;color:var(--ink);text-transform:uppercase;letter-spacing:1px;margin:2px 0 12px}
.about-text p{font-size:11.5px;line-height:19px;color:#555;margin-bottom:16px}

/* training */
.training{position:absolute;top:900px;left:0;width:1200px;height:840px;background:var(--white);text-align:center}
.training .eyebrow{margin-top:20px}
.training h2{font-family:var(--head);font-weight:700;font-size:30px;color:var(--ink);text-transform:uppercase;letter-spacing:1px;margin:2px 0 10px}
.training .lead{width:820px;margin:0 auto;font-size:11px;line-height:18px;color:#666}
.cards{position:absolute;top:190px;left:120px;width:960px;display:flex;align-items:center;gap:20px}
.arrow{width:28px;height:28px;border-radius:50%;border:1px solid #ccc;display:flex;align-items:center;justify-content:center}
.card{width:190px;height:150px;border:1px solid var(--line);display:flex;flex-direction:column;align-items:center;justify-content:center;gap:12px;padding:0 20px}
.card p{font-size:14px;color:var(--red);line-height:18px}
.range-photo{position:absolute;top:460px;left:200px;width:800px;height:370px;background:linear-gradient(120deg,#6f7480,#3b3e45 55%,#1d1e22);z-index:2}
.range-photo .play{left:380px;top:165px}

/* stories */
.stories{position:absolute;top:1740px;left:0;width:1200px;height:560px;background:linear-gradient(180deg,#141415,#222224)}
.stories-deco{position:absolute;right:0;top:160px;width:520px;height:340px;background:radial-gradient(ellipse at 60% 60%,rgba(180,140,80,.25),rgba(0,0,0,0) 70%)}
.stories-head{position:absolute;top:100px;width:100%;text-align:center}
.stories-head h2{font-family:var(--head);font-weight:700;font-size:32px;color:var(--white);text-transform:uppercase;letter-spacing:1px}
.quotes{position:absolute;top:200px;left:200px;width:800px;display:flex;gap:60px}
.quote{flex:1;color:#d6d6d6;font-size:11.5px;line-height:19px}
.quote .mark{font-family:var(--head);font-size:40px;color:var(--red);line-height:30px}
.quote .who{display:block;margin-top:16px;color:var(--red);font-style:italic}
.quote .date{color:#999;font-size:10.5px}
.dots{position:absolute;top:440px;width:100%;display:flex;justify-content:center;gap:8px}
.dots i{width:8px;height:8px;border-radius:50%;background:#555}
.dots i:first-child{background:var(--red)}

/* press */
.press{position:absolute;top:2300px;left:0;width:1200px;height:140px;background:#dcdcdc;display:flex;justify-content:center;align-items:center;gap:26px}
.press-box{width:200px;height:96px;background:var(--white);display:flex;align-items:center;justify-content:center;font-family:var(--head);font-weight:700;font-size:20px;color:var(--ink);text-align:center;line-height:20px}

/* footer */
.footer{position:absolute;top:2440px;left:0;width:1200px;height:244px;background:var(--ink);color:#bdbdbd}
.foot-brand{position:absolute;left:120px;top:40px;width:220px}
.foot-brand p{font-size:10.5px;line-height:17px;margin-top:14px}
.foot-col{position:absolute;top:40px}
.foot-col h4{font-family:var(--head);font-weight:700;font-size:16px;color:var(--white);margin-bottom:4px}
.foot-col .rule{width:26px;height:2px;background:var(--red);margin-bottom:14px}
.foot-col li{list-style:none;font-size:11px;line-height:22px;display:flex;align-items:center;gap:7px}
.email-row{display:flex;margin-top:4px}
.email-row .field{width:150px;height:30px;background:#2a2a2d;color:#888;font-size:10px;padding:9px 10px}
.email-row .btn{padding:9px 14px}
.copy{position:absolute;bottom:0;left:0;right:0;height:34px;border-top:1px solid #2a2a2d;text-align:center;font-size:9.5px;line-height:34px;color:#777}
</style>
</head>
<body>
<div class="page">

  <section class="hero">
    <div class="hero-visual" role="img" aria-label="Close-up of a matte black handgun on a dark surface"></div>
    <div class="play"><svg width="14" height="14" viewBox="0 0 14 14"><path d="M3 1 L12 7 L3 13Z" fill="var(--red)"/></svg></div>
    <h1>Make<br>Every Shot<br><em>Count</em></h1>
    <div class="actions">
      <span class="btn btn-red">Warrior Training</span>
      <span class="btn btn-white">Get Started</span>
    </div>
  </section>

  <header class="topbar">
    <div class="brand"><span class="dot"></span>Brisklane Wardens</div>
    <div class="contact-mini">
      <span><svg width="10" height="10" viewBox="0 0 10 10"><path d="M5 0a3.5 3.5 0 0 0-3.5 3.5C1.5 6 5 10 5 10s3.5-4 3.5-6.5A3.5 3.5 0 0 0 5 0z" fill="var(--red)"/></svg>P.O. Box 4120, Training Range</span>
      <span><svg width="10" height="10" viewBox="0 0 10 10"><path d="M2 0l2 2-1 2c1 1.5 2 2.5 3 3l2-1 2 2-1.5 2C4 9.5 .5 6 0 1.5z" fill="var(--red)"/></svg>(555) 014-2290</span>
    </div>
    <nav class="nav"><span>Home</span><span>Falcon Institute</span><span>Contact Us</span><span>Meet The Trainer</span></nav>
    <div class="search">Search here</div>
    <span class="btn btn-red">Join Newsletter</span>
  </header>

  <section class="about">
    <div class="portrait" role="img" aria-label="Portrait of instructor Morgan Pellbrook"></div>
    <div class="about-text">
      <div class="eyebrow">About the Instructor</div>
      <h2>Morgan Pellbrook</h2>
      <p>Morgan Pellbrook is a third generation firearms instructor and is proud to be part of this great community. He is a true security expert with over thirty years of experience in the industry. He has appeared on national news programs and has trained thousands of students across the region. He has been featured in many publications and has helped everyday people protect themselves and their loved ones from harm. He is a certified range safety officer and defensive pistol instructor. He often says: “My students are the heroes of their own story.”</p>
      <span class="btn btn-red">Learn More ›</span>
    </div>
  </section>

  <section class="training">
    <div class="eyebrow">Our 7 levels of Training</div>
    <h2>Take You From Zero To Hero</h2>
    <p class="lead">Want to learn something useful? Curious what the average person knows about concealed carry? Our levels take you from your first safe grip to calm decisions under pressure. We are talking about preparing you for real life and teaching you the skills and mindset needed to protect yourself and the people you love most.</p>
    <div class="cards">
      <div class="arrow"><svg width="8" height="10" viewBox="0 0 8 10"><path d="M6 1 L2 5 L6 9" stroke="#999" fill="none" stroke-width="1.5"/></svg></div>
      <div class="card"><svg width="34" height="34" viewBox="0 0 34 34"><circle cx="17" cy="17" r="14" stroke="var(--red)" fill="none" stroke-width="2"/><circle cx="17" cy="17" r="5" fill="var(--red)"/></svg><p>concealed carry class</p></div>
      <div class="card"><svg width="34" height="34" viewBox="0 0 34 34"><path d="M17 3 L17 31 M3 17 L31 17" stroke="var(--red)" stroke-width="2"/><circle cx="17" cy="17" r="9" stroke="var(--red)" fill="none" stroke-width="2"/></svg><p>Dynamic defensive shooting</p></div>
      <div class="card"><svg width="34" height="34" viewBox="0 0 34 34"><path d="M6 28 L28 6 M20 6 H28 V14" stroke="var(--red)" fill="none" stroke-width="2"/></svg><p>Fine tuning your technique</p></div>
      <div class="card"><svg width="34" height="34" viewBox="0 0 34 34"><rect x="4" y="7" width="26" height="18" rx="2" stroke="var(--red)" fill="none" stroke-width="2"/><path d="M12 30 H22" stroke="var(--red)" stroke-width="2"/></svg><p>Virtual threat lab</p></div>
      <div class="arrow"><svg width="8" height="10" viewBox="0 0 8 10"><path d="M2 1 L6 5 L2 9" stroke="#999" fill="none" stroke-width="1.5"/></svg></div>
    </div>
    <div class="range-photo" role="img" aria-label="Students practising at an indoor shooting range with paper targets">
      <div class="play"><svg width="14" height="14" viewBox="0 0 14 14"><path d="M3 1 L12 7 L3 13Z" fill="var(--red)"/></svg></div>
    </div>
  </section>

  <section class="stories">
    <div class="stories-deco" role="img" aria-label="Spent brass cartridges scattered on a dark table"></div>
    <div class="stories-head">
      <div class="eyebrow">Our</div>
      <h2>Success Stories</h2>
    </div>
    <div class="quotes">
      <div class="quote"><div class="mark">“</div>I felt nervous when I took the concealed carry class and left feeling confident. The instructor explained every step clearly and kept the range safe and friendly. Thank you for a great day of training!<span class="who">Margaret L.</span><span class="date">October 14, 2017</span></div>
      <div class="quote"><div class="mark">“</div>Took the course with my husband and loved every minute. We finally feel prepared and I know what to do if something goes wrong. Highly recommend this team to anyone.<span class="who">Denise R.</span><span class="date">October 11, 2017</span></div>
    </div>
    <div class="dots"><i></i><i></i><i></i></div>
  </section>

  <section class="press">
    <div class="press-box">Metro Newsline</div>
    <div class="press-box">Channel Nine News</div>
    <div class="press-box">Crestview Broadcast</div>
    <div class="press-box">Summit TV</div>
  </section>

  <footer class="footer">
    <div class="foot-brand">
      <div class="brand"><span class="dot"></span>Brisklane Wardens</div>
      <p>Our firearms instructor, carry instructor and training counselor helps civilians carry safely and with confidence.</p>
    </div>
    <div class="foot-col" style="left:440px">
      <h4>Our Links</h4><div class="rule"></div>
      <ul><li>Home</li><li>Falcon Institute</li><li>Contact Us</li><li>Meet The Trainer</li></ul>
    </div>
    <div class="foot-col" style="left:640px">
      <h4>Contact Us</h4><div class="rule"></div>
      <ul>
        <li><svg width="10" height="10" viewBox="0 0 10 10"><path d="M2 0l2 2-1 2c1 1.5 2 2.5 3 3l2-1 2 2-1.5 2C4 9.5 .5 6 0 1.5z" fill="var(--red)"/></svg>(555) 014-2290</li>
        <li><svg width="10" height="10" viewBox="0 0 10 10"><path d="M2 0l2 2-1 2c1 1.5 2 2.5 3 3l2-1 2 2-1.5 2C4 9.5 .5 6 0 1.5z" fill="var(--red)"/></svg>(555) 014-2291</li>
        <li><svg width="10" height="10" viewBox="0 0 10 10"><path d="M5 0a3.5 3.5 0 0 0-3.5 3.5C1.5 6 5 10 5 10s3.5-4 3.5-6.5A3.5 3.5 0 0 0 5 0z" fill="var(--red)"/></svg>P.O. Box 4120, Training Range</li>
      </ul>
    </div>
    <div class="foot-col" style="left:860px">
      <h4>Get In Touch</h4><div class="rule"></div>
      <div class="email-row"><div class="field">Enter your email</div><span class="btn btn-red">Submit</span></div>
    </div>
    <div class="copy">Copyright Brisklane Wardens 2017. All Rights Reserved</div>
  </footer>

</div>
</body>
</html>
```